Business card design for Bront Engineering Qavo

We need a new business card design along with all the necessary to place an order. The company is Bront Engineering Qavo and we recently updated our logo.

```html
<!DOCTYPE html>
<html lang="en">
<head>
<meta charset="utf-8">
<title>Bront Engineering Qavo – Business Card</title>
<link href="https://fonts.googleapis.com/css2?family=Poppins:wght@400;600;700&display=swap" rel="stylesheet">
<style>
  :root {
    --stage: #ffffff;
    --card-grey: #939393;
    --band-grey: #999999;
    --gold: #e0bf2a;
    --text-grey: #7a7a7a;
    --white: #ffffff;
    --rule: #c8c8c8;
  }
  * { margin: 0; padding: 0; box-sizing: border-box; }
  html, body {
    width: 979px; height: 1200px; overflow: hidden;
    background: var(--stage);
    font-family: "Poppins", sans-serif;
  }
  .canvas { position: relative; width: 979px; height: 1200px; }
  .card {
    position: absolute; left: 118px; width: 735px; height: 420px;
    box-shadow: 9px 9px 12px rgba(0,0,0,.32);
    overflow: hidden;
  }
  .card--front { top: 138px; background: var(--card-grey); }
  .card--back { top: 638px; background: var(--white); }

  .wordmark { font-weight: 600; line-height: 1; text-transform: uppercase; }
  .wordmark__main { display: block; }
  .wordmark__sub { display: block; }

  .card--front .wordmark {
    position: absolute; left: 0; right: 0; top: 168px;
    text-align: center; color: var(--white);
  }
  .card--front .wordmark__main { font-size: 58px; letter-spacing: 6px; }
  .card--front .wordmark__sub { font-size: 21px; letter-spacing: 2px; margin-top: 6px; }

  .accent-bar {
    position: absolute; left: 0; top: 76px; width: 8px; height: 49px;
    background: var(--card-grey);
  }
  .person { position: absolute; left: 36px; top: 76px; }
  .person__name { font-size: 24px; font-weight: 700; color: var(--gold); line-height: 1.2; }
  .person__role { font-size: 17px; color: var(--text-grey); line-height: 1.2; }

  .card--back .wordmark {
    position: absolute; right: 66px; top: 70px;
    text-align: right; color: var(--text-grey);
  }
  .card--back .wordmark__main { font-size: 40px; letter-spacing: 4px; }
  .card--back .wordmark__sub { font-size: 15px; letter-spacing: 1px; margin-top: 4px; }

  .accent-block {
    position: absolute; left: 62px; top: 262px; width: 120px; height: 120px;
    background: var(--gold);
  }

  .contact-rule {
    position: absolute; left: 669px; top: 214px; width: 1px; height: 143px;
    background: var(--rule);
  }
  .contacts {
    position: absolute; right: 90px; top: 280px; list-style: none;
  }
  .contacts li {
    display: flex; align-items: center; justify-content: flex-end;
    height: 27px; font-size: 18px; color: var(--text-grey);
  }
  .contacts svg { width: 18px; height: 18px; margin-left: 14px; fill: var(--gold); }

  .address-band {
    position: absolute; left: 0; right: 0; bottom: 0; height: 38px;
    background: var(--band-grey); color: var(--white);
    font-size: 18px; line-height: 38px; text-align: right; padding-right: 66px;
  }
</style>
</head>
<body>
<main class="canvas">
  <section class="card card--front">
    <div class="wordmark">
      <span class="wordmark__main">Bront</span>
      <span class="wordmark__sub">Engineering Qavo</span>
    </div>
  </section>

  <section class="card card--back">
    <div class="accent-bar"></div>
    <div class="person">
      <p class="person__name">Name Name</p>
      <p class="person__role">CEO</p>
    </div>

    <div class="wordmark">
      <span class="wordmark__main">Bront</span>
      <span class="wordmark__sub">Engineering Qavo</span>
    </div>

    <div class="accent-block"></div>
    <div class="contact-rule"></div>

    <ul class="contacts">
      <li>000-000-0000
        <svg viewBox="0 0 24 24" aria-hidden="true"><path d="M6.6 10.8a15.1 15.1 0 0 0 6.6 6.6l2.2-2.2a1 1 0 0 1 1-.25 11.4 11.4 0 0 0 3.6.57 1 1 0 0 1 1 1V20a1 1 0 0 1-1 1A17 17 0 0 1 3 4a1 1 0 0 1 1-1h3.5a1 1 0 0 1 1 1c0 1.25.2 2.45.57 3.57a1 1 0 0 1-.25 1z"/></svg>
      </li>
      <li>info@bront.com
        <svg viewBox="0 0 24 24" aria-hidden="true"><path d="M2 5h20v14H2z" opacity=".95"/><path d="M2 5l10 8 10-8" fill="none" stroke="#fff" stroke-width="1.8"/></svg>
      </li>
      <li>bront.com
        <svg viewBox="0 0 24 24" aria-hidden="true"><path d="M12 2a10 10 0 1 0 0 20 10 10 0 0 0 0-20zm0 2c.9 1.2 1.6 2.9 1.9 5h-3.8c.3-2.1 1-3.8 1.9-5zM9.9 4.4A12 12 0 0 0 8.1 9H4.6a8 8 0 0 1 5.3-4.6zm4.2 0A8 8 0 0 1 19.4 9h-3.5a12 12 0 0 0-1.8-4.6zM4.1 11h3.8a16 16 0 0 0 0 2H4.1a8 8 0 0 1 0-2zm5.9 0h4a14 14 0 0 1 0 2h-4a14 14 0 0 1 0-2zm6.1 0h3.8a8 8 0 0 1 0 2h-3.8a16 16 0 0 0 0-2zM4.6 15h3.5a12 12 0 0 0 1.8 4.6A8 8 0 0 1 4.6 15zm5.5 0h3.8c-.3 2.1-1 3.8-1.9 5-.9-1.2-1.6-2.9-1.9-5zm5.8 0h3.5a8 8 0 0 1-5.3 4.6 12 12 0 0 0 1.8-4.6z"/></svg>
      </li>
    </ul>

    <p class="address-band">3361 Address Street, City, Country Zip code</p>
  </section>
</main>
</body>
</html>
```